Website for Vayu Kiran Holdings

Need a project marketing website for our company which primarily deals in selling real estate(land sales) from Big Estates to Builders /Clients, help them in Building & Construction and do all Project Management.

Coding

Coded - Design and coding required

Number of Pages Required

4 page

Colors
0054AA
0677BA
7BADD7
CADEEF
E8F1F8
FFC000
F8CF3A
FAE287
FDF2CF
FEFAEE

```html
<!DOCTYPE html>
<html lang="en">
<head>
<meta charset="utf-8">
<title>Vayu Kiran Holdings</title>
<link href="https://fonts.googleapis.com/css2?family=Cinzel:wght@500;600&family=Open+Sans:wght@400;600;700&display=swap" rel="stylesheet">
<style>
:root{
  --blue-deep:#0054AA;
  --blue:#0677BA;
  --blue-soft:#7BADD7;
  --blue-pale:#CADEEF;
  --blue-mist:#E8F1F8;
  --navy:#0a2f6b;
  --ink:#1b1b1b;
  --grey:#6b6b6b;
  --line:#d5dce6;
  --white:#ffffff;
}
*{box-sizing:border-box;margin:0;padding:0}
html,body{width:1200px;height:4124px;overflow:hidden}
body{font-family:'Open Sans',Arial,sans-serif;color:var(--ink);background:var(--white)}
.page{position:relative;width:1200px;height:4124px;overflow:hidden;background:var(--white)}
.abs{position:absolute}
.serif{font-family:'Cinzel',Georgia,serif}

/* header */
.topbar{left:0;top:0;width:1200px;height:44px}
.topbar-item{top:11px;color:var(--white);font-size:15px;font-weight:600;display:flex;align-items:center;gap:10px}
.topbar-icon{width:24px;height:24px;border-radius:50%;background:var(--white);display:flex;align-items:center;justify-content:center}
.brand{left:145px;top:28px;display:flex;align-items:center;gap:14px}
.brand-mark{width:46px;height:46px;background:var(--blue-deep)}
.brand-name{font-size:24px;font-weight:700;color:var(--blue-deep);line-height:1.05;letter-spacing:1px}
.nav{left:520px;top:78px;display:flex;gap:0}
.nav a{font-size:13px;font-weight:600;color:#222;text-decoration:none;margin-right:30px;padding-bottom:6px}
.nav a.current{border-bottom:2px solid var(--blue-deep)}
.btn-nav{left:950px;top:71px;width:104px;height:33px;background:var(--blue-deep);color:var(--white);font-size:13px;font-weight:700;display:flex;align-items:center;justify-content:center;border-radius:3px;box-shadow:0 0 0 2px #fff,0 0 0 3px var(--blue-deep)}

/* hero */
.hero{left:0;top:122px;width:1200px;height:750px;background:linear-gradient(100deg,#0a3c8f 0%,#1657b3 35%,#3c7cc8 60%,#7fa4cf 80%,#b08e6e 100%)}
.hero-title{left:145px;top:230px;font-size:46px;line-height:61px;color:var(--white);font-weight:500;letter-spacing:1px}
.hero-sub{left:145px;top:372px;font-size:23px;line-height:33px;color:var(--white);font-weight:600}
.btn{display:flex;align-items:center;justify-content:center;font-weight:700;border-radius:3px}
.btn-hero-primary{left:145px;top:477px;width:158px;height:46px;background:var(--blue-deep);color:#fff;font-size:16px;box-shadow:0 0 0 2px var(--blue-deep) inset,0 0 0 3px #fff inset}
.btn-hero-secondary{left:330px;top:477px;width:158px;height:46px;background:#fff;color:var(--blue-deep);font-size:16px;box-shadow:0 0 0 2px #fff,0 0 0 3px var(--blue-deep)}
.slider-dot{left:1128px;width:8px;height:8px;border-radius:50%;background:#fff}
.slider-dot.ring{background:transparent;border:2px solid #fff;width:10px;height:10px;left:1127px}

/* section titles */
.section-title{width:1200px;left:0;text-align:center;font-size:44px;font-weight:500;color:var(--ink)}
.section-title .accent{color:var(--blue-deep)}

/* services */
.services-bg{left:0;top:860px;width:1200px;height:720px;background:linear-gradient(180deg,#fff 0%,#f3f7fc 45%,#dfe9f4 100%)}
.hex-card{width:285px;height:330px}
.hex-card svg.hex{position:absolute;left:0;top:0}
.hex-icon{position:absolute;left:112px;top:45px}
.hex-title{position:absolute;left:0;top:122px;width:285px;text-align:center;font-size:16px;font-weight:700}
.hex-text{position:absolute;left:30px;top:152px;width:225px;text-align:center;font-size:14.5px;line-height:24px;color:var(--grey)}
.hex-arrow{position:absolute;left:122px;top:272px;width:40px;height:40px;border-radius:6px;background:var(--blue-deep);display:flex;align-items:center;justify-content:center}
.pager-dot{top:1496px;width:10px;height:10px;border-radius:50%;background:#c8ccd3}
.pager-dot.on{background:var(--blue-deep)}

/* about */
.about-text{left:596px;top:1832px;width:460px;font-size:15.5px;line-height:27px;color:#fff;text-align:justify}
.about-title{left:596px;top:1745px;font-size:44px;color:#fff;font-weight:500}
.btn-about{left:598px;top:2033px;width:157px;height:46px;background:#fff;color:var(--blue-deep);font-size:15px;box-shadow:0 0 0 2px var(--blue-deep),0 0 0 3px #fff}

/* blog */
.blog-cell{width:303px;height:245px}
.blog-text{background:#fff;border-left:1px solid var(--line);border-right:1px solid var(--line);text-align:center}
.blog-text.featured{background:#d6e6f6;border:none}
.blog-title{position:absolute;left:0;top:44px;width:100%;font-size:16px;font-weight:600}
.blog-date{position:absolute;left:0;top:74px;width:100%;font-size:12.5px;color:var(--blue-deep);display:flex;justify-content:center;align-items:center;gap:5px}
.blog-excerpt{position:absolute;left:28px;top:100px;width:247px;font-size:12px;line-height:22px;color:#7a7a7a}
.btn-blog{position:absolute;left:102px;top:180px;width:110px;height:34px;background:var(--blue-deep);color:#fff;font-size:12px;box-shadow:0 0 0 2px var(--blue-deep) inset,0 0 0 3px #fff inset}
.blog-photo{width:303px;height:245px}

/* contact */
.contact-title{color:#fff}
.field{height:52px;background:#fff;font-size:15px;color:#444;padding:18px 20px 0}
.field.message{height:113px}
.btn-submit{left:522px;top:3422px;width:158px;height:48px;background:var(--blue-deep);color:#fff;font-size:16px;box-shadow:0 0 0 2px var(--blue-deep) inset,0 0 0 3px #fff inset,0 0 0 2px #fff}

/* footer */
.footer-bg{left:0;top:3560px;width:1200px;height:564px;background:linear-gradient(180deg,#eef1f5 0%,#fafbfc 40%,#fff 100%)}
.contact-item{top:3862px;display:flex;align-items:center;gap:16px;font-size:16px;color:#222}
.contact-circle{width:46px;height:46px;border-radius:50%;border:2px solid var(--blue-deep);display:flex;align-items:center;justify-content:center;background:#fff}
.contact-circle.solid{background:var(--blue-deep)}
.footer-nav{left:0;top:3945px;width:1200px;text-align:center;font-size:16.5px;font-weight:700;color:#222}
.footer-nav span.sep{margin:0 18px}
.copyright{left:0;top:3992px;width:1200px;text-align:center;font-size:13px;color:#333}
.copyright span{margin:0 8px}
.social{top:4024px;width:32px;height:32px;border-radius:50%;border:2px solid var(--blue-deep);background:#fff}
.social.solid{background:var(--blue-deep)}
.bottom-rule{left:0;top:4114px;width:1200px;height:10px;background:var(--blue-deep)}
</style>
</head>
<body>
<div class="page">

  <!-- header -->
  <svg class="abs topbar" width="1200" height="44" viewBox="0 0 1200 44"><polygon points="468,0 1200,0 1200,44 512,44" fill="#0054AA"/></svg>
  <div class="abs topbar-item" style="left:552px">
    <span class="topbar-icon"><svg width="14" height="14" viewBox="0 0 24 24"><path d="M6.6 10.8a15 15 0 0 0 6.6 6.6l2.2-2.2a1 1 0 0 1 1-.25 11.4 11.4 0 0 0 3.6.57 1 1 0 0 1 1 1V20a1 1 0 0 1-1 1A17 17 0 0 1 3 4a1 1 0 0 1 1-1h3.5a1 1 0 0 1 1 1c0 1.25.2 2.45.57 3.6a1 1 0 0 1-.25 1z" fill="#0054AA"/></svg></span>
    Call Us : +1 888 888 8888
  </div>
  <div class="abs topbar-item" style="left:788px">
    <span class="topbar-icon"><svg width="13" height="13" viewBox="0 0 24 24"><rect x="2" y="5" width="20" height="14" rx="2" fill="#0054AA"/><path d="M3 6l9 7 9-7" stroke="#fff" stroke-width="2" fill="none"/></svg></span>
    info@companyname.com
  </div>

  <div class="abs brand">
    <div class="brand-mark"></div>
    <div class="brand-name">VAYU KIRAN<br>HOLDINGS</div>
  </div>

  <nav class="abs nav">
    <a class="current" href="#">HOME</a>
    <a href="#">ABOUT US</a>
    <a href="#">SERVICES</a>
    <a href="#">NEWS</a>
    <a href="#">CONTACT US</a>
  </nav>
  <div class="abs btn-nav">APPLY NOW</div>

  <!-- hero -->
  <div class="abs hero" role="img" aria-label="City skyline at dusk beside a river with a gothic cathedral, tinted deep blue"></div>
  <h1 class="abs hero-title serif">INVEST IN YOUR FUTURE<br>WITH CONFIDENCE</h1>
  <p class="abs hero-sub">Tailored investment solutions for long-term<br>wealth in Australia and beyond</p>
  <div class="abs btn btn-hero-primary">APPLY NOW</div>
  <div class="abs btn btn-hero-secondary">LEARN MORE</div>
  <span class="abs slider-dot" style="top:416px"></span>
  <span class="abs slider-dot ring" style="top:434px"></span>
  <span class="abs slider-dot" style="top:456px"></span>

  <!-- services background -->
  <div class="abs services-bg"></div>
  <svg class="abs" style="left:0;top:630px" width="1200" height="250" viewBox="0 0 1200 250">
    <polygon points="0,228 600,16 1200,172 1200,250 0,250" fill="#0054AA"/>
    <polygon points="0,240 600,28 1200,184 1200,250 0,250" fill="#fff"/>
    <rect x="588" y="56" width="22" height="34" rx="11" fill="none" stroke="#333" stroke-width="2"/>
    <line x1="599" y1="64" x2="599" y2="72" stroke="#333" stroke-width="2"/>
    <polyline points="591,96 599,103 607,96" fill="none" stroke="#333" stroke-width="2"/>
    <polyline points="591,104 599,111 607,104" fill="none" stroke="#333" stroke-width="2"/>
  </svg>

  <h2 class="abs section-title serif" style="top:818px">OUR <span class="accent">SERVICES</span></h2>

  <!-- service cards -->
  <div class="abs hex-card" style="left:145px;top:913px">
    <svg class="hex" width="285" height="330" viewBox="0 0 285 330"><polygon points="142.5,1 284,72 284,258 142.5,329 1,258 1,72" fill="#fff" stroke="#d6dbe2" stroke-width="1.5"/></svg>
    <svg class="hex-icon" width="60" height="60" viewBox="0 0 60 60" fill="none" stroke="#0054AA" stroke-width="2"><rect x="8" y="26" width="36" height="26" rx="3"/><path d="M19 26v-5h14v5"/><line x1="8" y1="36" x2="44" y2="36"/><rect x="4" y="6" width="26" height="16"/><circle cx="46" cy="14" r="7"/></svg>
    <div class="hex-title">PORTFOLIO MANAGEMENT</div>
    <div class="hex-text">Sed ut perspiciatis unde omnis iste natus error sit voluptatem accusantium doloremntium dolorntiuolorque</div>
    <div class="hex-arrow"><svg width="16" height="18" viewBox="0 0 16 18" fill="none" stroke="#fff" stroke-width="2"><line x1="8" y1="1" x2="8" y2="16"/><polyline points="2,10 8,16 14,10"/></svg></div>
  </div>

  <div class="abs hex-card" style="left:458px;top:913px">
    <svg class="hex" width="285" height="330" viewBox="0 0 285 330"><polygon points="142.5,1 284,72 284,258 142.5,329 1,258 1,72" fill="#CADEEF" stroke="#c2d6ea" stroke-width="1.5"/></svg>
    <svg class="hex-icon" width="60" height="60" viewBox="0 0 60 60" fill="none" stroke="#0054AA" stroke-width="2"><rect x="12" y="26" width="6" height="12"/><rect x="22" y="20" width="6" height="18"/><rect x="32" y="14" width="6" height="24"/><polyline points="8,22 22,10 32,14 48,4"/><path d="M4 44c8-2 14 0 20 4h14c4 0 6-4 2-6l-10-2"/><path d="M38 46l14-8c3-2 5 1 3 3L40 54H8"/></svg>
    <div class="hex-title">INVESTMENT</div>
    <div class="hex-text">Sed ut perspiciatis unde omnis iste natus error sit voluptatem accusantium doloremntium dolorntiuolorque</div>
    <div class="hex-arrow"><svg width="16" height="18" viewBox="0 0 16 18" fill="none" stroke="#fff" stroke-width="2"><line x1="8" y1="1" x2="8" y2="16"/><polyline points="2,10 8,16 14,10"/></svg></div>
  </div>

  <div class="abs hex-card" style="left:770px;top:913px">
    <svg class="hex" width="285" height="330" viewBox="0 0 285 330"><polygon points="142.5,1 284,72 284,258 142.5,329 1,258 1,72" fill="#fff" stroke="#d6dbe2" stroke-width="1.5"/></svg>
    <svg class="hex-icon" width="60" height="60" viewBox="0 0 60 60" fill="none" stroke="#0054AA" stroke-width="2"><path d="M16 24a14 14 0 0 1 28 0z"/><line x1="12" y1="24" x2="48" y2="24"/><circle cx="30" cy="32" r="7"/><path d="M14 56c0-10 7-14 16-14s16 4 16 14"/><circle cx="12" cy="10" r="5"/></svg>
    <div class="hex-title">CONSTRUCTION</div>
    <div class="hex-text">Sed ut perspiciatis unde omnis iste natus error sit voluptatem accusantium doloremntium dolorntiuolorque</div>
    <div class="hex-arrow"><svg width="16" height="18" viewBox="0 0 16 18" fill="none" stroke="#fff" stroke-width="2"><line x1="8" y1="1" x2="8" y2="16"/><polyline points="2,10 8,16 14,10"/></svg></div>
  </div>

  <div class="abs hex-card" style="left:302px;top:1185px">
    <svg class="hex" width="285" height="330" viewBox="0 0 285 330"><polygon points="142.5,1 284,72 284,258 142.5,329 1,258 1,72" fill="#fff" stroke="#d6dbe2" stroke-width="1.5"/></svg>
    <svg class="hex-icon" width="60" height="60" viewBox="0 0 60 60" fill="none" stroke="#0054AA" stroke-width="2"><circle cx="18" cy="12" r="5"/><path d="M10 22l4 18h18l6 14"/><path d="M16 40l-6 14"/><line x1="6" y1="54" x2="44" y2="54"/><circle cx="46" cy="12" r="8"/></svg>
    <div class="hex-title">RETIREMENT PLANNING</div>
    <div class="hex-text">Sed ut perspiciatis unde omnis iste natus error sit voluptatem accusantium doloremntium dolorntiuolorque</div>
    <div class="hex-arrow"><svg width="16" height="18" viewBox="0 0 16 18" fill="none" stroke="#fff" stroke-width="2"><line x1="8" y1="1" x2="8" y2="16"/><polyline points="2,10 8,16 14,10"/></svg></div>
  </div>

  <div class="abs hex-card" style="left:614px;top:1185px">
    <svg class="hex" width="285" height="330" viewBox="0 0 285 330"><polygon points="142.5,1 284,72 284,258 142.5,329 1,258 1,72" fill="#fff" stroke="#d6dbe2" stroke-width="1.5"/></svg>
    <svg class="hex-icon" width="60" height="60" viewBox="0 0 60 60" fill="none" stroke="#0054AA" stroke-width="2"><path d="M30 44C20 32 16 26 16 18a14 14 0 0 1 28 0c0 8-4 14-14 26z"/><circle cx="30" cy="18" r="8"/><polygon points="4,48 30,40 56,48 30,58"/></svg>
    <div class="hex-title">LAND SALES</div>
    <div class="hex-text">Sed ut perspiciatis unde omnis iste natus error sit voluptatem accusantium doloremntium dolorntiuolorque</div>
    <div class="hex-arrow"><svg width="16" height="18" viewBox="0 0 16 18" fill="none" stroke="#fff" stroke-width="2"><line x1="8" y1="1" x2="8" y2="16"/><polyline points="2,10 8,16 14,10"/></svg></div>
  </div>

  <span class="abs pager-dot on" style="left:578px"></span>
  <span class="abs pager-dot" style="left:595px"></span>
  <span class="abs pager-dot" style="left:612px"></span>

  <!-- about -->
  <svg class="abs" style="left:0;top:1520px" width="1200" height="780" viewBox="0 0 1200 780">
    <defs>
      <linearGradient id="scenery" x1="0" y1="0" x2="0" y2="1"><stop offset="0" stop-color="#dfe9f4"/><stop offset="0.45" stop-color="#a9b6c6"/><stop offset="1" stop-color="#5f7a9c"/></linearGradient>
      <linearGradient id="aboutBlue" x1="0" y1="0" x2="1" y2="1"><stop offset="0" stop-color="#0a56b0"/><stop offset="1" stop-color="#0054AA"/></linearGradient>
      <linearGradient id="portrait" x1="0" y1="0" x2="1" y2="0"><stop offset="0" stop-color="#5b6d86"/><stop offset="0.5" stop-color="#2a3550"/><stop offset="1" stop-color="#1d3f78"/></linearGradient>
    </defs>
    <rect x="0" y="0" width="1200" height="260" fill="url(#scenery)" role="img" aria-label="Mountain range at sunset above a lake"/>
    <polygon points="0,205 600,32 1200,250 1200,780 0,780" fill="#fff"/>
    <g role="img" aria-label="Smiling businesswoman shaking hands with a client">
      <polygon points="0,222 600,40 600,765 0,545" fill="url(#portrait)"/>
    </g>
    <polygon points="600,40 1200,258 1200,545 600,765" fill="url(#aboutBlue)"/>
  </svg>
  <h2 class="abs about-title serif">ABOUT US</h2>
  <p class="abs about-text">Sed ut perspiciatis unde omnis iste natus error sit voluptatem accusantium doloremque laudantium, totam rem aperiam, eaque ipsa quae ab illo inventore veritatis et quasi architecto beatae vitae dicta sunt explicabo. Nemo enim ipsam voluptatem quia voluptas sit aspernatur aut odit aut fugit, sed quia consequuntur magni dolores eos qui ratione voluptatem sequi nesciunt.</p>
  <div class="abs btn btn-about">LEARN MORE</div>

  <!-- blog -->
  <h2 class="abs section-title serif" style="top:2370px">BLOG <span class="accent">POSTS</span></h2>

  <div class="abs blog-photo" style="left:145px;top:2470px;background:linear-gradient(180deg,#6f8fb2 0%,#c9a27a 55%,#e58a3a 70%,#3d3a3a 100%)" role="img" aria-label="Construction crane and workers on a site at sunset"></div>
  <div class="abs blog-cell blog-text featured" style="left:448px;top:2470px">
    <div class="blog-title">AT VERO EOS EACCUSAMU</div>
    <div class="blog-date"><svg width="11" height="11" viewBox="0 0 12 12" fill="none" stroke="#0054AA" stroke-width="1.4"><rect x="1" y="2" width="10" height="9"/><line x1="1" y1="5" x2="11" y2="5"/></svg>Jan 25,2019</div>
    <div class="blog-excerpt">At vero eos et accusamus et iusto odio dignissiducimumos ducimus qui blanditiis pducimuducimuraesentiu</div>
    <div class="btn btn-blog">LEARN MORE</div>
    <svg class="abs" style="left:141px;top:245px" width="22" height="11" viewBox="0 0 22 11"><polygon points="0,0 22,0 11,11" fill="#d6e6f6"/></svg>
  </div>
  <div class="abs blog-photo" style="left:751px;top:2470px;background:linear-gradient(135deg,#dfe4ea 0%,#a9b2bd 45%,#4b4f57 100%)" role="img" aria-label="Business team meeting around a glass table in a bright office"></div>

  <div class="abs blog-cell blog-text" style="left:145px;top:2715px">
    <div class="blog-title">AT VERO EOS EACCUSAMU</div>
    <div class="blog-date"><svg width="11" height="11" viewBox="0 0 12 12" fill="none" stroke="#0054AA" stroke-width="1.4"><rect x="1" y="2" width="10" height="9"/><line x1="1" y1="5" x2="11" y2="5"/></svg>Jan 25,2019</div>
    <div class="blog-excerpt">At vero eos et accusamus et iusto odio dignissiducimumos ducimus qui blanditiis pducimuducimuraesentiu</div>
    <div class="btn btn-blog">LEARN MORE</div>
  </div>
  <div class="abs blog-photo" style="left:448px;top:2715px;background:linear-gradient(135deg,#e8ecef 0%,#b4bcc4 40%,#2d3a4d 100%)" role="img" aria-label="Two advisers discussing in front of a bar chart display"></div>
  <div class="abs blog-cell blog-text" style="left:751px;top:2715px">
    <div class="blog-title">AT VERO EOS EACCUSAMU</div>
    <div class="blog-date"><svg width="11" height="11" viewBox="0 0 12 12" fill="none" stroke="#0054AA" stroke-width="1.4"><rect x="1" y="2" width="10" height="9"/><line x1="1" y1="5" x2="11" y2="5"/></svg>Jan 25,2019</div>
    <div class="blog-excerpt">At vero eos et accusamus et iusto odio dignissiducimumos ducimus qui blanditiis pducimuducimuraesentiu</div>
    <div class="btn btn-blog">LEARN MORE</div>
  </div>

  <!-- contact -->
  <div class="abs footer-bg"></div>
  <svg class="abs" style="left:0;top:2940px" width="1200" height="870" viewBox="0 0 1200 870">
    <defs>
      <linearGradient id="contactBlue" x1="0" y1="0" x2="0" y2="1"><stop offset="0" stop-color="#0d5cc4"/><stop offset="0.6" stop-color="#2a6fd0"/><stop offset="1" stop-color="#0054AA"/></linearGradient>
      <linearGradient id="harbour" x1="0" y1="0" x2="0" y2="1"><stop offset="0" stop-color="#5e8fd8"/><stop offset="0.5" stop-color="#2d62b8"/><stop offset="1" stop-color="#123f95"/></linearGradient>
    </defs>
    <polygon points="0,75 600,20 1200,60 1200,620 600,858 0,620" fill="url(#contactBlue)"/>
    <g role="img" aria-label="Harbour skyline with an opera house and city towers, tinted blue">
      <polygon points="0,480 1200,480 1200,620 600,858 0,620" fill="url(#harbour)"/>
    </g>
  </svg>
  <h2 class="abs section-title serif contact-title" style="top:3050px">CONTACT US</h2>
  <div class="abs field" style="left:233px;top:3140px;width:360px">First Name</div>
  <div class="abs field" style="left:605px;top:3140px;width:360px">Last Name</div>
  <div class="abs field" style="left:233px;top:3205px;width:360px">Email address</div>
  <div class="abs field" style="left:605px;top:3205px;width:360px">Phone Number</div>
  <div class="abs field message" style="left:233px;top:3270px;width:732px">Message</div>
  <div class="abs btn btn-submit">SUBMIT</div>

  <!-- footer -->
  <div class="abs contact-item" style="left:206px">
    <span class="contact-circle"><svg width="14" height="18" viewBox="0 0 14 18" fill="none" stroke="#0054AA" stroke-width="1.8"><path d="M7 17C2 11 1 8 1 6a6 6 0 0 1 12 0c0 2-1 5-6 11z"/><circle cx="7" cy="6" r="2"/></svg></span>
    <span style="font-size:16px;line-height:21px">234,Nemo enim ipsam volup<br>tatem quia volupta</span>
  </div>
  <div class="abs contact-item" style="left:518px">
    <span class="contact-circle solid"><svg width="16" height="16" viewBox="0 0 24 24"><path d="M6.6 10.8a15 15 0 0 0 6.6 6.6l2.2-2.2a1 1 0 0 1 1-.25 11.4 11.4 0 0 0 3.6.57 1 1 0 0 1 1 1V20a1 1 0 0 1-1 1A17 17 0 0 1 3 4a1 1 0 0 1 1-1h3.5a1 1 0 0 1 1 1c0 1.25.2 2.45.57 3.6a1 1 0 0 1-.25 1z" fill="#fff"/></svg></span>
    <span>+1 888 888 8888</span>
  </div>
  <div class="abs contact-item" style="left:740px">
    <span class="contact-circle"><svg width="16" height="14" viewBox="0 0 24 20"><rect x="1" y="2" width="22" height="16" rx="2" fill="#0054AA"/><path d="M2 4l10 7 10-7" stroke="#fff" stroke-width="2" fill="none"/></svg></span>
    <span>info@companyname.com</span>
  </div>

  <div class="abs footer-nav">HOME<span class="sep">/</span>ABOUT US<span class="sep">/</span>SERVICES<span class="sep">/</span>NEWS<span class="sep">/</span>CONTACT US<span class="sep">/</span>PRIVACY POLICY</div>
  <div class="abs copyright">Copyright 2025 Companyname.All Rights Reserved<span>|</span>Privacy Policy<span>|</span>Terms of Use</div>

  <span class="abs social" style="left:547px"></span>
  <span class="abs social solid" style="left:584px"></span>
  <span class="abs social" style="left:620px"></span>

  <div class="abs bottom-rule"></div>
</div>
</body>
</html>
```